Real Estate Agent needs business card design

We have logo designed already, want to have business card designed. Very interested in those smaller size business card as they look very trendy. Business name is called VORENDA REALTY

```html
<!DOCTYPE html>
<html lang="en">
<head>
<meta charset="utf-8">
<title>Vorenda Realty – Business Card</title>
<link rel="stylesheet" href="https://fonts.googleapis.com/css2?family=Cinzel:wght@500&family=Open+Sans:wght@400&display=swap">
<style>
  :root {
    --backdrop: #363636;
    --card: #252525;
    --gold: #c9a572;
    --name-grey: #b4b4b4;
    --text-grey: #a9a9a9;
    --brand-grey: #5c5c5c;
    --web-grey: #575757;
    --ink: #262626;
  }
  * { margin: 0; padding: 0; box-sizing: border-box; }
  html, body { width: 1200px; height: 800px; overflow: hidden; }
  body {
    background: var(--backdrop);
    font-family: "Open Sans", Arial, sans-serif;
    position: relative;
  }
  .card {
    position: absolute;
    top: 177px;
    width: 378px;
    height: 469px;
    border-radius: 34px;
    background: var(--card);
  }
  .card-front { left: 209px; }
  .card-back { left: 653px; }

  .brand-badge {
    position: absolute;
    left: 238px;
    top: 25px;
    width: 126px;
    height: 126px;
    border-radius: 50%;
    background: var(--gold);
    display: flex;
    align-items: center;
    justify-content: center;
  }
  .brand-badge-name {
    font-family: "Cinzel", Georgia, serif;
    font-weight: 500;
    font-size: 11px;
    letter-spacing: 0.5px;
    color: var(--ink);
    white-space: nowrap;
  }

  .agent-name {
    position: absolute;
    left: 19px;
    top: 204px;
    font-size: 25px;
    color: var(--name-grey);
    line-height: 1;
  }
  .agent-title {
    position: absolute;
    left: 19px;
    top: 241px;
    font-size: 16px;
    color: var(--gold);
    line-height: 1;
  }
  .contact-list {
    position: absolute;
    left: 19px;
    top: 296px;
    list-style: none;
  }
  .contact-item {
    display: flex;
    align-items: flex-start;
    font-size: 15.5px;
    line-height: 20px;
    color: var(--text-grey);
    margin-bottom: 12px;
  }
  .contact-icon {
    width: 18px;
    height: 20px;
    margin-right: 9px;
    flex: none;
    fill: var(--gold);
  }
  .gold-rule {
    position: absolute;
    left: 0;
    top: 408px;
    width: 279px;
    height: 3px;
    background: var(--gold);
  }
  .social-list {
    position: absolute;
    left: 289px;
    top: 402px;
    display: flex;
    gap: 13px;
  }
  .social-square {
    width: 14px;
    height: 14px;
    border-radius: 2px;
    background: var(--gold);
  }

  .brand-wordmark {
    position: absolute;
    left: 0;
    right: 0;
    top: 258px;
    text-align: center;
    font-family: "Cinzel", Georgia, serif;
    font-weight: 500;
    font-size: 34px;
    letter-spacing: 1px;
    color: var(--brand-grey);
    white-space: nowrap;
  }
  .brand-web {
    position: absolute;
    left: 0;
    right: 0;
    top: 351px;
    text-align: center;
    font-size: 13px;
    color: var(--web-grey);
  }
</style>
</head>
<body>
  <section class="card card-front">
    <div class="brand-badge"><span class="brand-badge-name">Vorenda Realty</span></div>

    <h1 class="agent-name">Clara Wendt</h1>
    <p class="agent-title">Senior Property Consultant</p>

    <ul class="contact-list">
      <li class="contact-item">
        <svg class="contact-icon" viewBox="0 0 18 20" aria-hidden="true">
          <path d="M1 8c0-3 3-4 8-4s8 1 8 4v1h-4V7.5H5V9H1z"/>
          <rect x="2" y="10" width="14" height="6" rx="1"/>
        </svg>
        <span>0400 555 127</span>
      </li>
      <li class="contact-item">
        <svg class="contact-icon" viewBox="0 0 18 20" aria-hidden="true">
          <path d="M1 6h16v1l-8 5-8-5z"/>
          <path d="M1 8.5l8 5 8-5V15H1z"/>
        </svg>
        <span>hello@vorenda.com</span>
      </li>
      <li class="contact-item">
        <svg class="contact-icon" viewBox="0 0 18 20" aria-hidden="true">
          <path d="M9 2a5.5 5.5 0 0 0-5.5 5.5C3.5 12 9 18 9 18s5.5-6 5.5-10.5A5.5 5.5 0 0 0 9 2zm0 7.6a2.1 2.1 0 1 1 0-4.2 2.1 2.1 0 0 1 0 4.2z"/>
        </svg>
        <span>7C, 48 Harbour Lane<br>Eastwood Bay, NSW 2199</span>
      </li>
    </ul>

    <div class="gold-rule"></div>
    <div class="social-list" aria-label="Social profiles">
      <span class="social-square"></span>
      <span class="social-square"></span>
      <span class="social-square"></span>
    </div>
  </section>

  <section class="card card-back">
    <p class="brand-wordmark">Vorenda Realty</p>
    <p class="brand-web">www.vorendarealty.com.au</p>
  </section>
</body>
</html>
```